Website for IT Security Company in Austria with small and medium business customer base

I own a one man IT security company with a customer small to medium business customer base and need a professional looking website that contains the following information:
- Home page: About the company....
- Services: The services that I offer. It would be nice to have icons if possible (e.g Quorel Ledger icon, digital certificate icon, ...) but this is not a must have.
- About me
- Blog: This is not a must have. It would be ok to just link it to an external blog.
- Impressum
- Contact: No form, just telephone number and e-mail address
- Anything else that you think is necessary for a professional appearance
Also I attached the company design. I do have all source files for the logo if required.

Target Market(s)

Small and medium business of all branches located in Austria

Industry/Entity Type

Cyber Security

Coding

Coded - Design and coding required

Number of Pages Required

5+ page

Font styles to use
Serif
Sans Serif
Other font styles liked:
• Bitsumishi, Bankgothic

Colors

Designer to choose only greyscale colors for use in the design.

Requirements
Must have
• The website must be a mobile-first design.
The design should not be too colorful or playful.
The logo should be used as much as possible
Navigation bar with multi drop-down menu for the services that I offer.
Example:
Services
-> Implementations
-> Implementation Service A
-> Implementation Service B
-> Security Audit
-> Audit A
-> Audit B
Maybe you could have service cards that describe the services briefly and on click redirect to the site that describes the service in detail.
End of example
Logo
contact
impressum
services that I offer
about me
about the company
Nice to have
• Icons would be nice (e.g. house for homepage, letter for contact, ...)
Also for the services I offer icons would be nice (Quorel Ledger, digtial certificates, hacking, security auditing)
For the fonts I have only sugested Bitsumishi and Bankgothic as they are part of my logo. No sure if you feel they make sense as part of the website
Should not have
• forms.
I want to the site to be made as easy as possible (HTML5, CSS, javascript/php/.net)
I do not want a wordpress template or suchlike.

```html
<!DOCTYPE html>
<html lang="en">
<head>
<meta charset="utf-8">
<title>Ferrite Bastion — Cyber Security &amp; IT Services</title>
<link rel="stylesheet" href="https://fonts.googleapis.com/css2?family=Orbitron:wght@500;700;800&family=Michroma&display=swap">
<style>
:root{
  --ink:#000000;
  --night:#0b0b0b;
  --coal:#1c1c1c;
  --slate:#2e2e2e;
  --accent:#8a8a8a;
  --accent-light:#bcbcbc;
  --white:#ffffff;
  --paper:#f3f3f3;
  --grey:#6b6b6b;
  --text:#333333;
  --line:#e0e0e0;
}
*{margin:0;padding:0;box-sizing:border-box}
html,body{width:1200px;height:4100px;overflow:hidden}
body{background:var(--white);font-family:"Michroma",sans-serif;color:var(--text);position:relative}
h1,h2,h3,.brand,.btn{font-family:"Orbitron",sans-serif;text-transform:uppercase}
.btn{display:inline-block;background:var(--slate);color:var(--white);font-size:12px;font-weight:700;letter-spacing:2px;padding:12px 26px;border-radius:3px}
.btn.on-dark{background:var(--accent-light);color:var(--ink)}
.btn.light{background:var(--white);color:var(--ink)}
p{font-size:12px;line-height:1.95;letter-spacing:.4px}

/* nav */
.topbar{position:absolute;top:0;left:0;width:1200px;height:48px;display:flex;align-items:center;justify-content:space-between;padding:0 40px;z-index:5}
.brand{display:flex;align-items:center;gap:10px;color:var(--white);font-size:18px;font-weight:700;letter-spacing:3px}
.brand-dot{width:14px;height:14px;background:var(--white)}
.menu{display:flex;gap:34px;list-style:none;font-size:10px;color:var(--white);letter-spacing:1.5px;text-transform:uppercase}

/* hero */
.hero{position:absolute;top:0;left:0;width:1200px;height:680px;background:linear-gradient(90deg,var(--night) 0%,#161616 55%,#262626 100%);overflow:hidden}
.hero-photo{position:absolute;right:0;top:0;width:620px;height:680px;background:radial-gradient(ellipse at 55% 45%,#5a5a5a 0%,#2a2a2a 45%,var(--night) 85%)}
.hero-copy{position:absolute;left:100px;top:200px;width:640px}
.hero h1{font-size:42px;font-weight:700;color:var(--accent-light);letter-spacing:4px;line-height:1.25;white-space:nowrap}
.hero h1 span{color:var(--white);display:block}
.hero p{color:#cfcfcf;margin:22px 0 34px;font-size:12px;width:500px}
.hero-edge{position:absolute;left:0;top:620px}

/* about company */
.about-co{position:absolute;top:720px;left:0;width:1200px;height:380px}
.hex-art{position:absolute;left:130px;top:30px;width:280px;height:300px;clip-path:polygon(50% 0,100% 25%,100% 75%,50% 100%,0 75%,0 25%);background:linear-gradient(135deg,#6a6a6a,#1f1f1f 60%,#8a8a8a)}
.about-co .copy{position:absolute;left:615px;top:40px;width:470px}
h2.title{font-size:26px;font-weight:700;color:var(--ink);letter-spacing:3px;margin-bottom:18px;white-space:nowrap}
h2.title em{font-style:normal;color:var(--accent)}
.copy p{margin-bottom:26px;font-size:11px}

/* services */
.services{position:absolute;top:1150px;left:0;width:1200px;height:560px;clip-path:polygon(0 0,44% 0,50% 5%,56% 0,100% 0,100% 100%,0 100%);overflow:hidden}
.svc-dark{position:absolute;left:0;top:0;width:640px;height:560px;background:linear-gradient(160deg,#2f2f2f,#101010 70%);clip-path:polygon(0 0,100% 0,88% 100%,0 100%)}
.svc-grey{position:absolute;right:0;top:0;width:640px;height:560px;background:linear-gradient(200deg,#7d7d7d,#4e4e4e 60%,#2c2c2c);clip-path:polygon(12% 0,100% 0,100% 100%,0 100%)}
.services h2{position:absolute;top:50px;width:1200px;text-align:center;color:var(--white);font-size:26px;letter-spacing:3px}
.svc{position:absolute;top:150px;width:360px;text-align:center;color:var(--white)}
.svc h3{font-size:20px;letter-spacing:2px;margin-bottom:18px}
.svc p{font-size:11px;color:#e6e6e6}
.svc.left{left:110px}
.svc.right{left:730px}
.services .btn{position:absolute;left:535px;top:455px}

/* about me */
.about-me{position:absolute;top:1760px;left:0;width:1200px;height:400px}
.about-me .copy{position:absolute;left:100px;top:40px;width:540px}
.portrait{position:absolute;left:700px;top:10px;width:340px;height:360px;clip-path:polygon(50% 0,100% 25%,100% 75%,50% 100%,0 75%,0 25%);background:linear-gradient(180deg,#e6e6e6,#8a8a8a 55%,#1c1c1c)}

/* testimonial */
.testimonials{position:absolute;top:2210px;left:0;width:1200px;height:440px;background:var(--paper)}
.testimonials h2{position:absolute;top:40px;width:1200px;text-align:center;font-size:26px;letter-spacing:3px;color:var(--ink)}
.cards{position:absolute;top:120px;left:190px;display:flex;gap:55px}
.t-card{width:240px;height:260px;background:var(--white);box-shadow:0 4px 14px rgba(0,0,0,.08);text-align:center;padding:26px 20px}
.avatar{width:44px;height:44px;border-radius:50%;background:linear-gradient(#cccccc,#707070);margin:0 auto 10px}
.t-name{font-size:9px;color:var(--ink);letter-spacing:1px}
.stars{color:var(--slate);font-size:14px;letter-spacing:2px;margin:6px 0 12px}
.t-card p{font-size:9px;line-height:1.9;color:var(--grey)}
.arrow{position:absolute;top:230px;width:32px;height:32px;border-radius:50%;background:#3a3a3a;display:flex;align-items:center;justify-content:center}
.arrow.prev{left:60px}.arrow.next{right:60px}

/* problem */
.problem{position:absolute;top:2680px;left:0;width:1200px;height:290px;background:var(--ink);text-align:center;color:var(--white)}
.problem h2{font-size:26px;letter-spacing:3px;margin-top:62px}
.problem p{width:760px;margin:14px auto 26px;font-size:11px;color:#d0d0d0}

/* blog */
.blog{position:absolute;top:3020px;left:0;width:1200px;height:540px;text-align:center}
.blog h2{font-size:26px;letter-spacing:3px;color:var(--ink)}
.blog .lead{width:620px;margin:10px auto 30px;font-size:10px;color:var(--grey)}
.posts{display:flex;gap:30px;justify-content:center}
.post{width:280px;text-align:left}
.post-img{height:200px}
.post-img.a{background:linear-gradient(135deg,#d2d2d2,#5e5e5e 60%,#2c2c2c)}
.post-img.b{background:radial-gradient(circle at 50% 50%,#dcdcdc,#505050 55%,#101010)}
.post-img.c{background:radial-gradient(circle at 50% 40%,#9a9a9a,#3a3a3a 55%,#0a0a0a)}
.post-meta{display:flex;justify-content:space-between;font-size:8px;color:var(--grey);margin:14px 0 8px;letter-spacing:1px}
.post h3{font-size:12px;color:var(--ink);letter-spacing:1px;margin-bottom:8px}
.post p{font-size:9px;line-height:1.8;color:var(--grey)}
.post-foot{display:flex;justify-content:space-between;font-size:8px;color:var(--grey);margin-top:14px;border-top:1px solid var(--line);padding-top:8px}
.post-foot b{color:var(--ink);font-weight:400}

/* footer */
.footer{position:absolute;top:3590px;left:0;width:1200px;height:510px;background:var(--ink);color:var(--white)}
.footer-edge{position:absolute;top:-2px;left:0}
.f-brand{position:absolute;left:120px;top:130px;width:220px;text-align:center}
.f-brand .mark{width:60px;height:60px;border:3px solid var(--white);margin:0 auto 14px}
.f-brand .brand{justify-content:center;font-size:16px}
.f-col{position:absolute;top:110px}
.f-col h3{font-size:15px;letter-spacing:2px;margin-bottom:22px}
.f-col ul{list-style:none;font-size:10px;line-height:2.4;color:#d0d0d0}
.f-col li{display:flex;align-items:flex-start;gap:10px}
.f-col.links{left:385px}
.f-col.contact{left:600px;width:280px}
.f-col.follow{left:925px}
.socials{display:flex;gap:12px}
.socials span{width:18px;height:18px;border-radius:50%;background:var(--white)}
.copyright{position:absolute;bottom:0;left:0;width:1200px;height:46px;border-top:1px solid #222;text-align:center;font-size:8px;letter-spacing:1px;color:#9a9a9a;line-height:46px}
</style>
</head>
<body>

<header class="topbar">
  <div class="brand"><span class="brand-dot"></span>Ferrite Bastion</div>
  <ul class="menu">
    <li>Home</li><li>Services ▾</li><li>About Me</li><li>Blog</li><li>Impressum</li><li>Contact Us</li>
  </ul>
</header>

<section class="hero">
  <div class="hero-photo" role="img" aria-label="Photo of a consultant in glasses thinking in a dim office"></div>
  <div class="hero-copy">
    <h1>Cyber Sercurity <span>&amp; IT Services</span></h1>
    <p>IT security is a set of cybersecurity strategies that prevents unauthorized access to organizational assets, such as computers, networks, and data.</p>
    <span class="btn on-dark">Get Started</span>
  </div>
  <svg class="hero-edge" width="1200" height="60" viewBox="0 0 1200 60" aria-hidden="true">
    <path d="M0 60 L0 30 L420 30 L470 52 L730 52 L780 30 L1200 30 L1200 60Z" fill="#ffffff"/>
    <path d="M0 30 L420 30 L470 52 L730 52 L780 30 L1200 30" fill="none" stroke="#8a8a8a" stroke-width="4"/>
  </svg>
</section>

<section class="about-co">
  <div class="hex-art" role="img" aria-label="Digital security illustration in a hexagon frame"></div>
  <div class="copy">
    <h2 class="title">About <em>Ferrite Bastion</em></h2>
    <p>We protect small and medium businesses across Austria with clear, honest security work. From network hardening and identity setup to certificates and audits, every project is planned with care, explained in plain words and delivered on time, so your team can work safely while your systems stay steady, monitored and ready for tomorrow.</p>
    <span class="btn">Learn More</span>
  </div>
</section>

<section class="services">
  <div class="svc-dark" role="img" aria-label="Dark photo of hands typing on a laptop keyboard"></div>
  <div class="svc-grey" role="img" aria-label="Backdrop with a glowing padlock on a circuit board"></div>
  <h2>Service We Offer</h2>
  <div class="svc left">
    <h3>Implementations</h3>
    <p>Quorel Ledger setups, digital certificates and secure networks built to fit your business. We plan, install and document every step, so each system works reliably and your staff knows exactly how to use it day to day.</p>
  </div>
  <div class="svc right">
    <h3>Security Audit</h3>
    <p>Careful checks of your servers, accounts and devices to find weak spots before attackers do. You receive a clear report with ranked findings, practical fixes and a follow up review to confirm that each risk is truly closed.</p>
  </div>
  <span class="btn light">Learn More</span>
</section>

<section class="about-me">
  <div class="copy">
    <h2 class="title">About <em>Me</em></h2>
    <p>I am an independent security engineer with many years of hands on work in business networks. I set up directories, certificates and firewalls, test systems the way an attacker would, and train teams to spot threats early. Each client works with me directly, from the first call to the final report, which keeps projects personal, fast and fully accountable for every single result delivered.</p>
    <span class="btn">Learn More</span>
  </div>
  <div class="portrait" role="img" aria-label="Portrait of the founder in a dark suit inside a hexagon frame"></div>
</section>

<section class="testimonials">
  <h2>Testimonial</h2>
  <div class="arrow prev"><svg width="12" height="12" viewBox="0 0 12 12"><path d="M8 1 L3 6 L8 11" stroke="#fff" stroke-width="2" fill="none"/></svg></div>
  <div class="cards">
    <div class="t-card"><div class="avatar"></div><div class="t-name">Marten Vollgrub</div><div class="stars">★★★★★</div><p>Clear advice, fast work and a setup that simply runs. Our office feels much safer now and every question got a patient answer.</p></div>
    <div class="t-card"><div class="avatar"></div><div class="t-name">Marten Vollgrub</div><div class="stars">★★★★★</div><p>The audit found issues we never knew about. The report was easy to follow and every fix was done within the same week.</p></div>
    <div class="t-card"><div class="avatar"></div><div class="t-name">Marten Vollgrub</div><div class="stars">★★★★★</div><p>Professional, friendly and reliable. Our certificates and accounts are finally in order and we sleep better at night.</p></div>
  </div>
  <div class="arrow next"><svg width="12" height="12" viewBox="0 0 12 12"><path d="M4 1 L9 6 L4 11" stroke="#fff" stroke-width="2" fill="none"/></svg></div>
</section>

<section class="problem">
  <h2>Have Any Problem?</h2>
  <p>Call or write anytime. We answer quickly, look at your situation together and find a safe, practical solution for your business systems and your team.</p>
  <span class="btn on-dark">Get Started</span>
</section>

<section class="blog">
  <h2>Latest Blog</h2>
  <p class="lead">Notes on threats, tools and good habits for keeping small business networks secure every day.</p>
  <div class="posts">
    <article class="post">
      <div class="post-img a" role="img" aria-label="Photo of charts and a laptop on a desk"></div>
      <div class="post-meta"><span>Data Analysis</span><span>Mar 12</span></div>
      <h3>Data Analysis</h3>
      <p>How log data reveals early signs of intrusion and what to watch weekly.</p>
      <div class="post-foot"><span>Admin</span><b>Read More →</b></div>
    </article>
    <article class="post">
      <div class="post-img b" role="img" aria-label="Photo of a glowing digital lock graphic"></div>
      <div class="post-meta"><span>Security</span><span>Mar 08</span></div>
      <h3>Cyber Hacks</h3>
      <p>Common attack tricks used on small firms and simple ways to stop them.</p>
      <div class="post-foot"><span>Admin</span><b>Read More →</b></div>
    </article>
    <article class="post">
      <div class="post-img c" role="img" aria-label="Photo of a hooded figure in front of glowing code"></div>
      <div class="post-meta"><span>Security</span><span>Mar 02</span></div>
      <h3>Cyber Hacks</h3>
      <p>Why phishing still works and how short staff training cuts the risk.</p>
      <div class="post-foot"><span>Admin</span><b>Read More →</b></div>
    </article>
  </div>
</section>

<footer class="footer">
  <svg class="footer-edge" width="1200" height="40" viewBox="0 0 1200 40" aria-hidden="true">
    <path d="M0 0 L1200 0 L1200 10 L780 10 L740 34 L460 34 L420 10 L0 10Z" fill="#ffffff"/>
    <path d="M0 10 L420 10 L460 34 L740 34 L780 10 L1200 10" fill="none" stroke="#8a8a8a" stroke-width="4"/>
  </svg>
  <div class="f-brand">
    <div class="mark"></div>
    <div class="brand">Ferrite Bastion</div>
  </div>
  <div class="f-col links">
    <h3>Quick Links</h3>
    <ul><li>Home</li><li>Services</li><li>Privacy Policy</li><li>Blogs</li><li>Contacts</li></ul>
  </div>
  <div class="f-col contact">
    <h3>Contact Us</h3>
    <ul>
      <li><svg width="14" height="14" viewBox="0 0 14 14" style="margin-top:8px"><path d="M3 1 L5.5 1 L6.5 4 L5 5.2 C5.8 7 7 8.2 8.8 9 L10 7.5 L13 8.5 L13 11 C13 12 12 13 11 13 C6 12.5 1.5 8 1 3 C1 2 2 1 3 1Z" fill="none" stroke="#bcbcbc" stroke-width="1.3"/></svg>+43 1 555 0182</li>
      <li><svg width="14" height="14" viewBox="0 0 14 14" style="margin-top:8px"><rect x="1" y="3" width="12" height="8" fill="none" stroke="#bcbcbc" stroke-width="1.4"/><path d="M1 3 L7 8 L13 3" fill="none" stroke="#bcbcbc" stroke-width="1.4"/></svg>hello@ferritebastion.example</li>
      <li><svg width="14" height="14" viewBox="0 0 14 14" style="margin-top:8px"><path d="M7 13 C3 8 2 6 2 5 A5 5 0 0 1 12 5 C12 6 11 8 7 13Z" fill="none" stroke="#bcbcbc" stroke-width="1.4"/><circle cx="7" cy="5" r="1.6" fill="#bcbcbc"/></svg>14 Kesselgasse,<br>Lindorf 4127</li>
    </ul>
  </div>
  <div class="f-col follow">
    <h3>Follow Us</h3>
    <div class="socials"><span></span><span></span><span></span><span></span></div>
  </div>
  <div class="copyright">Copyright 2024. All Rights Reserved Ferrite Bastion</div>
</footer>

</body>
</html>
```